Store Bill board

We have a 10' x 29' sign off of a major highway that we need a billboard designed for. We have had a few preliminary desgins but want something really eye catching as you have less than a second in many cases to catch people's eyes. We have different logos and pics that a designer can choose and design with. It has to also have a 'Visit Our Store' on the bottom right and corner with an arrow. We like the Locally Built , locally born logo but would want the font much bigger and the Colorado flag underneath bigger. We'd like to see our logo say 'custom electric bikes' underneath the GrivO-Rides logo rather than 'fat tire electric bikes'

```html
<!DOCTYPE html>
<html lang="en">
<head>
<meta charset="utf-8">
<title>GrivO-Rides Highway Billboard</title>
<link href="https://fonts.googleapis.com/css2?family=Oswald:wght@500;600;700&display=swap" rel="stylesheet">
<style>
  :root {
    --orange: #f06a24;
    --ink: #111111;
    --charcoal: #2b2b2b;
    --slate: #4a4a4a;
    --paper: #f3f3f4;
    --stage: #d9dde2;
    --flag-blue: #0f2f8c;
    --flag-red: #d21f2a;
    --flag-gold: #f7c51a;
    --white: #ffffff;
  }
  * { margin: 0; padding: 0; box-sizing: border-box; }
  html, body { width: 1200px; height: 700px; overflow: hidden; }
  body {
    background: var(--stage);
    font-family: "Oswald", "Arial Narrow", sans-serif;
    position: relative;
  }
  .billboard {
    position: absolute;
    left: 0; top: 143px;
    width: 1200px; height: 414px;
    background: var(--paper);
    overflow: hidden;
  }
  .billboard__art { position: absolute; inset: 0; }
  .brand {
    position: absolute;
    left: 650px; top: 38px;
    width: 520px;
    display: flex; align-items: center; justify-content: center; gap: 14px;
  }
  .brand__dot {
    width: 42px; height: 42px; border-radius: 50%;
    background: var(--orange);
  }
  .brand__name {
    font-weight: 700; font-size: 50px; line-height: 1;
    color: var(--ink); letter-spacing: 0.5px;
  }
  .headline {
    position: absolute;
    left: 630px; top: 126px;
    width: 560px;
    text-align: center;
    font-weight: 700; text-transform: uppercase;
    line-height: 1; font-size: 70px;
    color: var(--ink);
    white-space: nowrap;
  }
  .headline__accent { color: var(--orange); }
  .cta {
    position: absolute;
    left: 740px; top: 292px;
    width: 340px; height: 88px;
  }
  .cta__shape { position: absolute; inset: 0; }
  .cta__label {
    position: absolute; left: 0; top: 12px; width: 100%;
    text-align: center;
    font-weight: 600; font-size: 34px; line-height: 1;
    color: var(--ink); text-transform: uppercase;
  }
  .origin {
    position: absolute;
    left: 24px; top: 344px;
  }
  .origin__text {
    color: var(--white); font-weight: 500;
    font-size: 27px; line-height: 1.05; text-transform: uppercase;
  }
</style>
</head>
<body>
  <section class="billboard" aria-label="GrivO-Rides billboard">
    <svg class="billboard__art" width="1200" height="414" viewBox="0 0 1200 414">
      <defs>
        <linearGradient id="photoTone" x1="0" y1="0" x2="1" y2="1">
          <stop offset="0" stop-color="#c4b3a6"/>
          <stop offset="0.5" stop-color="#d9773f"/>
          <stop offset="1" stop-color="#6f645d"/>
        </linearGradient>
      </defs>
      <polygon class="stripe-dark" points="420,0 500,0 620,414 540,414" fill="var(--slate)"/>
      <polygon class="stripe-light" points="500,0 512,0 632,414 620,414" fill="var(--white)"/>
      <polygon class="stripe-orange" points="515,0 575,0 610,90 550,90" fill="var(--orange)"/>
      <polygon class="stripe-orange-low" points="560,350 600,350 625,414 585,414" fill="var(--orange)"/>
      <g role="img" aria-label="Photo of a rider on an orange fat-tire electric bike, close-up of the front wheel">
        <polygon points="0,0 440,0 560,414 0,414" fill="url(#photoTone)"/>
      </g>
      <polygon class="origin-panel" points="0,326 330,326 360,414 0,414" fill="var(--charcoal)"/>
      <g class="flag" transform="translate(200,340)">
        <rect width="84" height="60" fill="var(--flag-blue)"/>
        <rect y="20" width="84" height="20" fill="var(--white)"/>
        <circle cx="32" cy="30" r="17" fill="var(--flag-red)"/>
        <polygon points="32,30 52,18 52,42" fill="var(--white)"/>
        <circle cx="32" cy="30" r="9" fill="var(--flag-gold)"/>
      </g>
    </svg>

    <div class="brand">
      <span class="brand__dot"></span>
      <span class="brand__name">GRIVO-RIDES</span>
    </div>

    <h1 class="headline">Custom <span class="headline__accent">Electric</span><br>Bikes</h1>

    <div class="cta">
      <svg class="cta__shape" width="340" height="88" viewBox="0 0 340 88">
        <path d="M0,0 L340,0 L336,22 Q330,44 300,54 L170,88 L40,54 Q10,44 4,22 Z" fill="var(--orange)"/>
      </svg>
      <span class="cta__label">Visit Our Store</span>
    </div>

    <div class="origin">
      <p class="origin__text">Locally Built<br>Locally Born</p>
    </div>
  </section>
</body>
</html>
```